Dorlin Commercial Truck / Trailer / RV Repair

Need a billboard design for our shop. Will include our logo below and want the word DORLIN on the top without the circle. Straighten out the letter "M" on the logo as well. Also will include a rough draft of a design and words I had in mind. All the words need to be included but the layout and design is up to you. Open to all options just needs to be easy to see and understand the message from the highway.

```html
<!DOCTYPE html>
<html lang="en">
<head>
<meta charset="utf-8">
<title>Dorlin Commercial Repair Shop – Billboards</title>
<link href="https://fonts.googleapis.com/css2?family=Alfa+Slab+One&family=Michroma&family=Montserrat:ital,wght@0,500;0,700;0,800;1,800&family=Oswald:wght@500&family=Russo+One&display=swap" rel="stylesheet">
<style>
  :root {
    --backdrop: #7fadd6;
    --brand-blue: #3b82c9;
    --brand-blue-dark: #2f6fb4;
    --steel-gray: #6f6f6f;
    --light-gray: #c9c9cb;
    --ink: #111214;
    --paper: #ffffff;
    --night-teal: #1d3f4c;
  }
  * { box-sizing: border-box; margin: 0; padding: 0; }
  html, body { width: 1200px; height: 1200px; overflow: hidden; }
  body { background: var(--backdrop); position: relative; font-family: "Montserrat", sans-serif; }

  .billboard {
    position: absolute; left: 57px; width: 1085px; height: 270px;
    background: var(--paper); overflow: hidden;
    box-shadow: 0 3px 8px rgba(0,0,0,.25);
  }
  .billboard--light { top: 264px; }
  .billboard--dark  { top: 603px; }
  .billboard svg.shapes { position: absolute; inset: 0; }
  .abs { position: absolute; white-space: nowrap; }

  /* ---------- Light billboard ---------- */
  .light-name {
    left: 31px; top: 20px; color: var(--paper);
    font-family: "Michroma", sans-serif; font-size: 50px; letter-spacing: 2px;
  }
  .light-parking {
    left: 33px; top: 238px; color: var(--paper);
    font-family: "Russo One", sans-serif; font-size: 13.5px; letter-spacing: 2.6px;
  }
  .light-headline {
    left: 533px; top: 26px; color: var(--brand-blue);
    font-family: "Alfa Slab One", serif; font-size: 53px; letter-spacing: 3px;
    transform: scaleX(.9); transform-origin: left;
  }
  .light-subhead {
    left: 791px; top: 82px; width: 264px; height: 28px;
    background: var(--steel-gray); color: var(--paper);
    font-family: "Russo One", sans-serif; font-size: 19px; letter-spacing: 4px;
    display: flex; align-items: center; justify-content: center;
  }
  .service-label {
    top: 128px; font-family: "Russo One", sans-serif; font-size: 10px;
    letter-spacing: 1px; color: #444; border-bottom: 1px solid #555; width: 110px;
  }
  .light-phone {
    left: 622px; top: 203px; color: var(--brand-blue);
    font-family: "Alfa Slab One", serif; font-size: 25px; letter-spacing: 1.5px;
  }
  .light-quote {
    left: 735px; top: 240px; width: 214px; height: 18px;
    background: var(--steel-gray); color: var(--paper);
    font-family: "Russo One", sans-serif; font-size: 10px; letter-spacing: 1px;
    display: flex; align-items: center; justify-content: flex-end; padding-right: 12px;
    clip-path: polygon(4% 0, 100% 0, 97% 100%, 0 100%);
  }

  /* ---------- Dark billboard ---------- */
  .dark-name {
    left: 132px; top: 16px; color: var(--brand-blue);
    font-family: "Montserrat", sans-serif; font-weight: 800; font-size: 36px; letter-spacing: 1px;
  }
  .dark-headline {
    left: 30px; top: 50px; color: var(--paper);
    font-family: "Montserrat", sans-serif; font-weight: 800; font-style: italic; font-size: 51px;
  }
  .dark-headline .accent { color: var(--brand-blue); }
  .dark-rule { left: 32px; top: 115px; width: 196px; height: 1px; background: var(--paper); }
  .dark-subhead {
    left: 228px; top: 100px; color: var(--brand-blue);
    font-family: "Montserrat", sans-serif; font-weight: 800; font-style: italic; font-size: 23px;
  }
  .service-tile {
    top: 143px; width: 109px; height: 79px; border: 2px solid var(--paper);
    border-radius: 3px;
  }
  .service-caption {
    top: 231px; width: 109px; text-align: center;
    font-weight: 700; font-size: 13px; color: #222; letter-spacing: .5px;
  }
  .dark-phone {
    left: 483px; top: 148px; color: var(--paper);
    font-family: "Oswald", sans-serif; font-weight: 500; font-size: 31px; letter-spacing: 0;
  }
  .dark-quote {
    left: 431px; top: 194px; width: 260px; height: 25px; background: var(--brand-blue);
    color: var(--paper); font-size: 10.5px; font-weight: 500; letter-spacing: 1px;
    display: flex; align-items: center; padding-left: 17px;
  }
  .dark-parking {
    left: 431px; top: 232px; color: #222;
    font-family: "Montserrat", sans-serif; font-weight: 500; font-size: 21px;
  }

  /* ---------- Brand mark ---------- */
  .brand-mark { display: flex; align-items: center; gap: 5px; }
  .brand-mark .dot {
    width: 10px; height: 10px; border-radius: 50%; border: 2px solid var(--steel-gray);
  }
  .brand-mark .word {
    font-family: "Montserrat", sans-serif; font-weight: 700; font-size: 17px;
    color: var(--brand-blue); letter-spacing: .5px;
  }
</style>
</head>
<body>

<section class="billboard billboard--light" aria-label="Dorlin commercial repair shop billboard, light version">
  <svg class="shapes" width="1085" height="270" viewBox="0 0 1085 270">
    <defs>
      <linearGradient id="nightRoad" x1="0" y1="0" x2="1" y2="1">
        <stop offset="0" stop-color="#4a5d66"/>
        <stop offset=".45" stop-color="#1d3f4c"/>
        <stop offset="1" stop-color="#0f2530"/>
      </linearGradient>
    </defs>
    <polygon points="0,0 345,0 505,270 0,270" fill="url(#nightRoad)" role="img" aria-label="Photo of a blue semi truck with trailer driving on a highway at night"/>
    <polygon points="345,0 390,0 555,270 505,270" fill="var(--brand-blue)"/>
    <polygon points="300,0 330,0 330,18" fill="var(--brand-blue-dark)"/>
    <polygon points="40,80 95,80 165,190 130,190" fill="var(--brand-blue)" opacity=".85"/>
    <polygon points="935,0 990,0 1085,130 1085,195" fill="var(--light-gray)"/>
    <polygon points="987,0 1030,0 1085,70 1085,115" fill="var(--brand-blue)"/>
    <polygon points="1045,0 1060,0 1085,35 1085,55" fill="var(--light-gray)"/>
    <polygon points="535,143 655,143 679,198 559,198" fill="#7d8c78" role="img" aria-label="Photo of a white truck on a highway"/>
    <polygon points="661,143 784,143 808,198 685,198" fill="#b86b3c" role="img" aria-label="Photo of a truck and trailer in the desert"/>
    <polygon points="785,143 920,143 944,198 809,198" fill="#9a7a63" role="img" aria-label="Photo of an RV in a canyon landscape"/>
    <polygon points="920,170 947,170 923,198 896,198" fill="var(--steel-gray)"/>
    <g transform="translate(574,210)" fill="none" stroke="var(--steel-gray)" stroke-width="3">
      <circle cx="18" cy="18" r="17"/>
      <path d="M11 9 l4 0 l2 5 l-3 2 a12 12 0 0 0 6 6 l2 -3 l5 2 l0 4 a2 2 0 0 1 -2 2 a18 18 0 0 1 -16 -16 a2 2 0 0 1 2 -2z" stroke-width="2"/>
    </g>
  </svg>

  <div class="abs light-name">DORLIN</div>
  <div class="abs light-parking">PARKING &amp; STORAGE AVAILABLE</div>
  <div class="abs light-headline">COMMERCIAL</div>
  <div class="abs light-subhead">REPAIR SHOP</div>
  <div class="abs service-label" style="left:532px">TRUCKS</div>
  <div class="abs service-label" style="left:657px">TRAILERS</div>
  <div class="abs service-label" style="left:781px">RV</div>
  <div class="abs light-phone">555.014.2290</div>
  <div class="abs light-quote">OR COME BY FOR A QUOTE!</div>
  <div class="abs brand-mark" style="left:962px; top:208px;">
    <span class="dot"></span><span class="word">DORLIN</span>
  </div>
</section>

<section class="billboard billboard--dark" aria-label="Dorlin commercial repair shop billboard, dark version">
  <svg class="shapes" width="1085" height="270" viewBox="0 0 1085 270">
    <defs>
      <linearGradient id="sunsetSky" x1="0" y1="0" x2="1" y2="1">
        <stop offset="0" stop-color="#a9a48e"/>
        <stop offset=".55" stop-color="#d9b37a"/>
        <stop offset="1" stop-color="#8c4a3a"/>
      </linearGradient>
      <linearGradient id="facets" x1="0" y1="0" x2="1" y2="1">
        <stop offset="0" stop-color="#202225"/>
        <stop offset="1" stop-color="#0b0c0d"/>
      </linearGradient>
    </defs>
    <rect x="0" y="0" width="1085" height="198" fill="url(#facets)"/>
    <polygon points="0,0 260,0 120,120" fill="#1a1c1f"/>
    <polygon points="260,0 520,0 380,150" fill="#16181b"/>
    <polygon points="380,150 520,0 690,0 560,198" fill="#1c1e21"/>
    <polygon points="687,0 1085,0 1085,190 960,215 740,210 583,101" fill="var(--paper)"/>
    <polygon points="712,0 1085,0 1085,200 1000,212 745,203 610,101" fill="url(#sunsetSky)" role="img" aria-label="Photo of a red semi truck with a container trailer on a road at sunset"/>
    <polygon points="1000,218 1085,204 1085,228" fill="var(--light-gray)"/>
    <g transform="translate(433,150)" fill="none" stroke="var(--brand-blue)" stroke-width="2.2">
      <circle cx="17" cy="18" r="15"/>
      <path d="M8 14 l4 0 l2 4 l-2 2 a9 9 0 0 0 5 5 l2 -2 l4 2 l0 4 a2 2 0 0 1 -2 2 a15 15 0 0 1 -13 -13z"/>
      <rect x="24" y="0" width="14" height="9" rx="2"/>
    </g>
  </svg>

  <div class="abs dark-name">DORLIN</div>
  <div class="abs dark-headline">CO<span class="accent">M</span>MERCIAL</div>
  <div class="abs dark-rule"></div>
  <div class="abs dark-subhead">REPAIR SHOP</div>

  <div class="abs service-tile" style="left:29px; background:#8a5a3e;" role="img" aria-label="Photo of a truck hauling a shipping container"></div>
  <div class="abs service-tile" style="left:160px; background:#c9883f;" role="img" aria-label="Photo of a truck and trailer on a desert road"></div>
  <div class="abs service-tile" style="left:291px; background:#6b7a86;" role="img" aria-label="Photo of a travel trailer in the mountains"></div>
  <div class="abs service-caption" style="left:29px">TRUCKS</div>
  <div class="abs service-caption" style="left:160px">TRAILERS</div>
  <div class="abs service-caption" style="left:291px">RV</div>

  <div class="abs dark-phone">555.014.2290</div>
  <div class="abs dark-quote">CALL OR COME BY FOR A QUOTE!</div>
  <div class="abs dark-parking">PARKING &amp; STORAGE AVAILABLE</div>
  <div class="abs brand-mark" style="left:982px; top:38px;">
    <span class="dot"></span><span class="word">DORLIN</span>
  </div>
</section>

</body>
</html>
```